Design gusset bag packaging for a high protein cake mix

We need packaging designed for a 4x6x2 3/8 silver metallic bag. It will hold high protein cake mix. I will attach current label designs that we have on the back. I want it to be catchy-- template will be posted as well. Please stick to 6 printing colors or less.

Target Market(s)

Fitness, diet, dessert

Font styles to use
Serif
Decorative
Script

Colors
86cfc6
87d0c7
33b8a4
f0494f
fbf289
f59195
85cae6

Requirements
Must have
• It must include the nutrition label. I will attach our current label. Must have our logo. Please change the title to Tiny Oak Bakery Cake Mix (it's in red on the label) and change applesauce serving to 1/2 cup from "1 serving". Please stick to 6 printing colors or less.
Nice to have
• Would love to top flap above the zipper to say Eat Cake, Get Oaky! And on the back top flap say "Sprinkles- Enjoy the little things in life" Would love to have some sprinkles scattered around the front of the package..maybe even to look like it's coming out of a sprinkle shaker. Please feel free to use a more modern looking font

```html
<!DOCTYPE html>
<html lang="en">
<head>
<meta charset="utf-8">
<title>Tiny Oak Bakery Cake Mix – Pouch Packaging</title>
<link rel="stylesheet" href="https://fonts.googleapis.com/css2?family=Lilita+One&family=Open+Sans:wght@400;600;700&display=swap">
<style>
  :root{
    --stage:#d9d9d9;
    --bag:#ffffff;
    --aqua:#a9dbe6;
    --red:#f0494f;
    --pink:#f59195;
    --yellow:#fbf289;
    --teal:#86cfc6;
    --ink:#1d1d1f;
    --deep:#1f3d44;
  }
  *{box-sizing:border-box;margin:0;padding:0}
  html,body{width:1200px;height:966px;overflow:hidden;background:var(--stage)}
  body{position:relative;font-family:"Open Sans",Arial,sans-serif;color:var(--ink)}
  .pouch{position:absolute;top:190px;width:390px;height:586px;background:var(--bag);overflow:hidden}
  .pouch--front{left:190px}
  .pouch--back{left:620px}
  .sprinkle-field{position:absolute;inset:0;background:
      radial-gradient(circle at 18% 30%,rgba(240,73,79,.22),transparent 28%),
      radial-gradient(circle at 82% 38%,rgba(134,207,198,.30),transparent 28%),
      radial-gradient(circle at 15% 72%,rgba(251,242,137,.45),transparent 26%),
      radial-gradient(circle at 86% 74%,rgba(245,145,149,.28),transparent 26%),
      radial-gradient(circle at 50% 12%,rgba(134,207,198,.22),transparent 30%)}
  .zipper{position:absolute;left:0;right:0;top:112px;height:42px;border-top:1px solid #eee;border-bottom:1px solid #eee;background:repeating-linear-gradient(#fff 0 6px,#f1f1f1 6px 8px)}
  .flap-title{position:absolute;left:0;right:0;text-align:center;font-family:"Lilita One",cursive;font-weight:400;color:var(--deep);text-shadow:2px 0 0 var(--aqua),-2px 0 0 var(--aqua),0 2px 0 var(--aqua),0 -2px 0 var(--aqua),2px 2px 0 var(--aqua),-2px -2px 0 var(--aqua),2px -2px 0 var(--aqua),-2px 2px 0 var(--aqua)}
  .pouch--front .flap-title{top:52px;font-size:37px}
  .pouch--back .flap-title{top:28px;font-size:28px;line-height:1.3}

  .brand{position:absolute;left:0;right:0;text-align:center;font-weight:700;color:var(--ink)}
  .brand__dot{display:block;margin:0 auto;border-radius:50%;background:var(--aqua)}
  .pouch--front .brand{top:238px;font-size:40px;line-height:42px}
  .pouch--front .brand__dot{width:22px;height:22px;margin-bottom:10px}

  .title-band{position:absolute;left:0;right:0;top:390px;height:78px;background:var(--aqua);text-align:center;font-weight:700;font-size:42px;line-height:78px;color:var(--red);letter-spacing:1px}
  .claims{position:absolute;left:0;right:0;top:482px;text-align:center;font-size:15px;line-height:22px;font-weight:600}
  .foot-band{position:absolute;left:0;right:0;bottom:0;height:36px;background:var(--aqua);text-align:center;font-size:15px;font-weight:600;line-height:36px;color:var(--deep);letter-spacing:.5px}

  /* back */
  .info{position:absolute;left:24px;top:166px;width:176px}
  .info__title{text-align:center;color:var(--red);font-size:16px;line-height:20px}
  .info__brand{text-align:center;font-weight:700;font-size:22px;line-height:26px;margin:16px 0 18px}
  .info__brand .brand__dot{width:16px;height:16px;margin-bottom:6px}
  .info h4{font-size:7.5px;font-weight:700}
  .info p{font-size:7.5px;line-height:9.6px;text-align:justify;margin-bottom:12px}
  .net-wt{position:absolute;left:36px;top:512px;font-size:10px;font-weight:600}

  .nutrition{position:absolute;left:210px;top:168px;width:148px;border:1px solid var(--ink);padding:2px 3px;font-size:6px;line-height:8px;background:#fff}
  .nutrition h3{font-size:15px;line-height:16px;font-weight:700}
  .rule-thick{border-top:4px solid var(--ink);margin:2px 0}
  .rule-mid{border-top:2px solid var(--ink);margin:2px 0}
  .nutrition table{width:100%;border-collapse:collapse}
  .nutrition td{border-top:1px solid #888;padding:1px 0}
  .nutrition td.n{text-align:right;width:24px;font-weight:600}
  .nutrition .indent{padding-left:6px}
  .nutrition .b{font-weight:700}
  .nutrition .fine{font-size:5px;line-height:6.5px;margin-top:2px}
  .address{position:absolute;left:234px;top:504px;width:104px;text-align:center;font-size:7px;line-height:8px;font-weight:700}
  .social{position:absolute;left:0;right:0;bottom:0;height:34px;background:var(--aqua);display:flex;justify-content:center;align-items:center;gap:16px;font-size:13px;color:var(--deep)}
  .social__mark{display:inline-block;width:18px;height:18px;background:#2a7f94;border-radius:3px;vertical-align:middle;margin-right:4px}
</style>
</head>
<body>

<section class="pouch pouch--front" aria-label="Front of pouch">
  <div class="sprinkle-field" role="img" aria-label="Colourful sprinkles scattered across the pouch"></div>
  <h1 class="flap-title">Eat Cake, Get Oaky!</h1>
  <div class="zipper"></div>
  <div class="brand"><span class="brand__dot"></span>Tiny Oak<br>Bakery</div>
  <div class="title-band">CAKE MIX</div>
  <div class="claims">26g of protein<br>gluten-free<br>microwaveable</div>
  <div class="foot-band">www.tinyoakbakery.com</div>
</section>

<section class="pouch pouch--back" aria-label="Back of pouch">
  <div class="sprinkle-field" role="img" aria-label="Colourful sprinkles scattered across the pouch"></div>
  <h2 class="flap-title">Sprinkles make<br>everything better</h2>
  <div class="zipper" style="top:130px"></div>

  <div class="info">
    <div class="info__title">Tiny Oak Bakery<br>Cake Mix</div>
    <div class="info__brand"><span class="brand__dot"></span>Tiny Oak<br>Bakery</div>
    <h4>Baking Instructions:</h4>
    <p>Add 1 egg white (3 Tbsp), 1/2 cup unsweetened applesauce (75g) and 1/8th cup of unsweet cashew milk (30mL/g). Bake in microwave for 2:40</p>
    <p><b>INGREDIENTS:</b> Whey Protein Blend (Whey Protein Isolate, Whey Protein Concentrate, Whey Protein Hydrolysate), Natural And Artificial Flavors, Salt, Xanthan Gum, Sucralose, Essential Fatty Acid Matrix (Medium Chain Triglycerides, Conjugated Linoleic Acid), Digestive Enzyme Complex (Glycoamylase, Amylase, Lipase, Protease, Papain, Hemicellulase, Cellulase, Lactase), Stevia Leaf Extract, Coconut Flour, Organic Golden Flax Seed Meal, Baking Powder (Sodium Acid Pyrophosphate, Sodium Bicarbonate, Cornstarch, Monocalcium Phosphate) Contains Milk</p>
  </div>
  <div class="net-wt">Net Wt: 2.2 oz (60g)</div>

  <div class="nutrition">
    <h3>Nutrition Facts</h3>
    <div>Serving Size: (60g)<br>Servings Per Container: 1</div>
    <div class="rule-thick"></div>
    <table>
      <tr><td class="b">Amount Per Serving</td><td class="n">Mix</td><td class="n">Baked</td></tr>
      <tr><td class="b">Calories</td><td class="n">180</td><td class="n">250</td></tr>
      <tr><td class="indent">Calories from Fat</td><td class="n">50</td><td class="n">50</td></tr>
    </table>
    <div class="rule-mid"></div>
    <table>
      <tr><td></td><td class="n" colspan="2" style="width:48px">% Daily Value**</td></tr>
      <tr><td><b>Total Fat</b> 5g*</td><td class="n">8%</td><td class="n">9%</td></tr>
      <tr><td class="indent">Saturated Fat 2g</td><td class="n">10%</td><td class="n">10%</td></tr>
      <tr><td class="indent"><i>Trans</i> Fat 0g</td><td class="n"></td><td class="n"></td></tr>
      <tr><td><b>Cholesterol</b> 55mg</td><td class="n">18%</td><td class="n">18%</td></tr>
      <tr><td><b>Sodium</b> 370mg</td><td class="n">15%</td><td class="n">20%</td></tr>
      <tr><td><b>Total Carbohydrate</b> 11g</td><td class="n">4%</td><td class="n">7%</td></tr>
      <tr><td class="indent">Dietary Fiber 7g</td><td class="n">28%</td><td class="n">32%</td></tr>
      <tr><td class="indent">Sugars 3g</td><td class="n"></td><td class="n"></td></tr>
      <tr><td><b>Protein</b> 26g</td><td class="n"></td><td class="n"></td></tr>
    </table>
    <div class="rule-thick"></div>
    <table>
      <tr><td>Vitamin A</td><td class="n">0%</td><td class="n">2%</td></tr>
      <tr><td>Vitamin C</td><td class="n">0%</td><td class="n">15%</td></tr>
      <tr><td>Calcium</td><td class="n">25%</td><td class="n">30%</td></tr>
      <tr><td>Iron</td><td class="n">6%</td><td class="n">6%</td></tr>
    </table>
    <div class="fine">* Amount in Mix<br>**Percent Daily Values based on a 2,000 calorie diet.</div>
    <table class="fine">
      <tr><td></td><td>Calories:</td><td>2,000</td><td>2,500</td></tr>
      <tr><td>Total Fat</td><td>Less than</td><td>65g</td><td>80g</td></tr>
      <tr><td>Sat Fat</td><td>Less than</td><td>20g</td><td>25g</td></tr>
      <tr><td>Cholesterol</td><td>Less than</td><td>300mg</td><td>300mg</td></tr>
      <tr><td>Sodium</td><td>Less than</td><td>2,400mg</td><td>2,400mg</td></tr>
      <tr><td>Total Carbohydrate</td><td></td><td>300g</td><td>375g</td></tr>
      <tr><td>Dietary Fiber</td><td></td><td>25g</td><td>30g</td></tr>
    </table>
  </div>
  <div class="address">TINY OAK BAKERY<br>PO BOX 512<br>MAPLE GROVE, OH<br>44100<br>www.tinyoakbakery.com</div>

  <div class="social"><span><span class="social__mark"></span>@tinyoakbakery</span><span>#tinyoakbakery</span></div>
</section>

</body>
</html>
```